Marlowe's Classic Dressing

We are looking for a new label as we switch or glass bottle from a traditional bottle to a round bottle. We want to create a newer/ more appealing logo, while still maintaining some of our old label features to ensure that the brand awareness is not lost. We like the coloring of the blue and white, but feel free to play around with other colors in the design.
We are looking to add product features to our label such as "Gluten-Free", "Original Recipe From 1957" "Family Owned". With this being an older company we would like to keep the traditional feel of our label with some added modern touches.
We are not married to the greek logo/ building but would love some designs with and without it.
WE ARE LOOKING FOR A ROUND LABEL. The pictures provided below are of the old bottle.
There is a picture of the ringneck bottle below. The size of the label is 4.00 x 7.00.

```html
<!DOCTYPE html>
<html lang="en">
<head>
<meta charset="utf-8">
<title>Marlowe's Classic Dressing – Label Options</title>
<link href="https://fonts.googleapis.com/css2?family=Josefin+Sans:wght@300;400;600&display=swap" rel="stylesheet">
<style>
  :root {
    --navy: #2b3c7c;
    --navy-deep: #22316a;
    --red: #d55656;
    --white: #ffffff;
    --cream: #f4ecec;
    --rule: #c85a5a;
    --stone: #7f8fc4;
  }
  * { margin: 0; padding: 0; box-sizing: border-box; }
  html, body { width: 1200px; height: 776px; overflow: hidden; background: var(--white); }
  body { position: relative; font-family: "Josefin Sans", sans-serif; color: var(--white); }

  .label {
    position: absolute;
    top: 208px;
    width: 200px;
    height: 360px;
    background: var(--navy);
    overflow: hidden;
    text-align: center;
  }
  .label--emblem { left: 130px; }
  .label--banner { left: 508px; }
  .label--temple { left: 886px; }

  .red-band { position: absolute; left: 0; right: 0; background: var(--red); }
  .pattern-strip {
    position: absolute; left: 0; right: 0; height: 8px;
    background: linear-gradient(var(--cream), #dfe2f0);
  }

  .brand {
    position: absolute; left: 0; right: 0;
    font-weight: 600; font-size: 25px; letter-spacing: 0.5px;
    color: var(--white);
  }
  .title {
    position: absolute; left: 0; right: 0;
    font-weight: 400; font-size: 50px; line-height: 1; letter-spacing: 1px;
  }
  .subtitle {
    position: absolute; left: 0; right: 0;
    font-weight: 400; font-size: 17px; letter-spacing: 5px;
  }
  .features {
    position: absolute; left: 35px; right: 35px;
    font-size: 7.5px; letter-spacing: 1px; line-height: 13px;
    text-transform: uppercase;
    border-top: 1px solid var(--rule); border-bottom: 1px solid var(--rule);
    padding: 2px 0;
  }
  .claim {
    position: absolute; left: 0; right: 0;
    font-size: 9px; letter-spacing: 1.2px;
  }
  .volume {
    position: absolute; left: 0; right: 0;
    font-size: 6.5px; letter-spacing: 0.6px;
  }

  /* Option 1 – medallion */
  .label--emblem .red-band { top: 0; height: 82px; }
  .label--emblem .pattern-strip { top: 82px; }
  .medallion {
    position: absolute; left: 50%; top: 12px; width: 116px; height: 116px;
    margin-left: -58px; border-radius: 50%;
    background: var(--white); border: 5px solid var(--red);
  }
  .medallion-art {
    position: absolute; inset: 8px; border-radius: 50%;
    background: linear-gradient(180deg, var(--red) 0%, #e9a0a0 38%, var(--stone) 55%, var(--navy-deep) 100%);
  }
  .label--emblem .brand { top: 134px; }
  .label--emblem .title { top: 170px; }
  .label--emblem .subtitle { top: 219px; }
  .label--emblem .features { top: 244px; }
  .label--emblem .claim { top: 293px; }
  .label--emblem .volume { top: 328px; }

  /* Option 2 – banner */
  .label--banner .strip-top { top: 0; }
  .label--banner .red-band { top: 8px; height: 90px; }
  .label--banner .strip-mid { top: 98px; }
  .label--banner .strip-bottom { bottom: 6px; }
  .label--banner .brand { top: 38px; font-size: 28px; }
  .label--banner .title { top: 140px; }
  .label--banner .subtitle { top: 190px; }
  .label--banner .features { top: 236px; }
  .label--banner .claim { top: 282px; }
  .label--banner .volume { top: 318px; }

  /* Option 3 – temple band */
  .label--temple .red-band { top: 0; height: 64px; }
  .temple-art {
    position: absolute; left: 40px; top: 12px; width: 120px; height: 50px;
    background: linear-gradient(180deg, #e4b0b0 0%, var(--stone) 45%, var(--navy) 100%);
  }
  .label--temple .pattern-strip { top: 64px; }
  .label--temple .brand { top: 102px; }
  .label--temple .title { top: 148px; }
  .label--temple .subtitle { top: 198px; }
  .label--temple .features { top: 244px; }
  .label--temple .claim { top: 292px; }
  .label--temple .volume { top: 326px; }
</style>
</head>
<body>

  <section class="label label--emblem">
    <div class="red-band"></div>
    <div class="pattern-strip" role="img" aria-label="Greek key border pattern"></div>
    <div class="medallion">
      <div class="medallion-art" role="img" aria-label="Illustration of a classical Greek temple on a hill"></div>
    </div>
    <div class="brand">Marlowe's</div>
    <div class="title">GREEK</div>
    <div class="subtitle">DRESSING</div>
    <div class="features">Original recipe from 1957<br>Family owned</div>
    <div class="claim">GLUTEN-FREE</div>
    <div class="volume">8FL. OZ. (237 ml)</div>
  </section>

  <section class="label label--banner">
    <div class="pattern-strip strip-top" role="img" aria-label="Wave border pattern"></div>
    <div class="red-band"></div>
    <div class="pattern-strip strip-mid" role="img" aria-label="Greek key border pattern"></div>
    <div class="brand">Marlowe's</div>
    <div class="title">GREEK</div>
    <div class="subtitle">DRESSING</div>
    <div class="features">Original recipe from 1957<br>Family owned</div>
    <div class="claim">GLUTEN-FREE</div>
    <div class="volume">8FL. OZ. (237 ml)</div>
    <div class="pattern-strip strip-bottom" role="img" aria-label="Wave border pattern"></div>
  </section>

  <section class="label label--temple">
    <div class="red-band"></div>
    <div class="temple-art" role="img" aria-label="Illustration of a classical Greek temple"></div>
    <div class="pattern-strip" role="img" aria-label="Greek key border pattern"></div>
    <div class="brand">Marlowe's</div>
    <div class="title">GREEK</div>
    <div class="subtitle">DRESSING</div>
    <div class="features">Original recipe from 1957<br>Family owned</div>
    <div class="claim">GLUTEN-FREE</div>
    <div class="volume">8FL. OZ. (237 ml)</div>
  </section>

</body>
</html>
```